Lantern - Web Design Project

We are seeking to have our website redesigned. Our current webpage is rather dated looking www.lantern-outcomes.com We will be utilizing similar content to explain our services as what is in the website now. We do not see it at a retail portal but rather a website for those inquiring about our services as a reference check so to speak.

We wish to have a look that is considered clean, fresh, contemporary and contains a business savvy vibe.

We prefer isolated white background and also wish to retain the integrity of our Logo and colour scheme.

We are looking for something that doesnt look like it was designed at home on sitemoose. We are hoping to find something that looks like it would reside on a tablet.
Updates

Hello designers!

We apologize for our tardiness as we have been quite preoccupied. We will be extending our invites to the end of January!

Hello All,

Please review our offer once again for updated requirements.  We are hoping to accept a design by months end.

Lantern

Target Market(s)

Business to business clients and Large manufacturers

Industry/Entity Type

Retail

Requirements
Must have
• Existing Logo

There must be an area dedicated to an intro video that will be incorporated on our landing page.

We require design of the other pages as well not only the landing page.

```html
<!DOCTYPE html>
<html lang="en">
<head>
<meta charset="utf-8">
<title>Lantern Performance Group</title>
<link rel="stylesheet" href="https://fonts.googleapis.com/css2?family=Open+Sans:ital,wght@0,400;0,600;0,700;1,800&family=Yanone+Kaffeesatz:wght@400&display=swap">
<style>
:root{
  --red:#e4463a;
  --red-nav:#f2321a;
  --ink:#222;
  --text:#555;
  --light-bg:#f0f0f0;
  --footer:#3b3b3b;
  --rule:#c8c8c8;
  --social:#c9c9c9;
  --hero-tone:#c9cdd2;
  --people-tone:#8a8f96;
  --tree-tone:#8fb06a;
}
*{margin:0;padding:0;box-sizing:border-box}
html,body{width:748px;height:1200px;overflow:hidden;background:#fff}
body{position:relative;font-family:"Open Sans",Arial,sans-serif;color:var(--text)}
.abs{position:absolute}

/* header */
.site-header{left:0;top:0;width:748px;height:71px;background:#fff}
.brand{left:46px;top:24px;display:flex;align-items:center;gap:5px;font-size:19px;font-weight:600;color:#444;letter-spacing:-.3px;line-height:22px}
.brand-dot{width:8px;height:8px;border-radius:50%;background:var(--red)}
.social{left:157px;top:30px;display:flex;gap:3px}
.social span{width:21px;height:21px;border-radius:50%;background:var(--social)}
.nav{left:261px;top:0;height:71px;font-size:8px;color:#555}
.nav a{text-decoration:none;color:inherit;line-height:74px;position:absolute;white-space:nowrap}
.nav .home{left:0;width:52px;height:71px;background:var(--red-nav);color:#fff;font-weight:700;text-align:center}
.nav .signin{color:var(--red-nav);font-weight:600}

/* intro video / slider */
.hero{left:0;top:71px;width:748px;height:239px;background:var(--light-bg)}
.intro-video{left:46px;top:9px;width:660px;height:221px;background:linear-gradient(100deg,#eef0f2 0%,var(--hero-tone) 45%,#eef0f2 100%)}
.play-button{left:306px;top:87px;width:48px;height:48px}
.hero-caption{left:329px;top:163px;width:331px;height:44px;background:rgba(25,25,25,.85);color:#fff;text-align:right;padding:10px 12px 0 0;font-size:8px;line-height:13px}
.hero-caption b{font-weight:700}
.arrow{top:95px;width:24px;height:24px}
.arrow.prev{left:15px}
.arrow.next{left:710px}

/* welcome */
.welcome{left:96px;top:321px;width:560px;text-align:center}
.welcome h1{font-family:"Yanone Kaffeesatz",sans-serif;font-weight:400;color:var(--red);font-size:17px;margin-bottom:6px}
.welcome p{font-size:8.6px;line-height:13px;color:#333}
.welcome p+p{margin-top:13px}

/* who we are */
.who{left:0;top:450px;width:748px;height:252px;background:var(--red)}
.section-title{font-weight:800;font-style:italic;font-size:23px;color:var(--ink);letter-spacing:-.3px}
.section-title em{color:var(--red)}
.who .section-title{position:absolute;left:46px;top:21px;color:#fff}
.who-text{left:46px;top:60px;width:476px;color:#fff;font-size:8.4px;line-height:13px}
.who-text p+p{margin-top:13px}
.who-photo{left:537px;top:27px;width:167px;height:211px;background:var(--people-tone)}

/* performance */
.perf-title{left:46px;top:732px}
.perf-text{left:46px;top:785px;width:448px;font-size:8.4px;line-height:13px}
.perf-text p+p{margin-top:13px}
.solution-list{left:537px;top:741px;width:158px;list-style:none;font-size:8.2px;color:#555}
.solution-list li{height:16.2px;line-height:15px;border-bottom:1px dashed var(--rule);padding-left:8px;position:relative}
.solution-list li::before{content:"";position:absolute;left:1px;top:5px;border-left:3px solid #888;border-top:3px solid transparent;border-bottom:3px solid transparent}
.solution-list li.active{color:var(--red)}
.solution-list li.active::before{border-left-color:var(--red)}

/* sustain */
.sustain{left:0;top:918px;width:748px;height:240px;background:var(--light-bg)}
.sustain .section-title{position:absolute;left:46px;top:10px}
.sustain-photo{left:46px;top:55px;width:157px;height:161px;background:var(--tree-tone)}
.sustain-text{left:227px;top:55px;width:472px;font-size:8.4px;line-height:13px}
.sustain-text p+p{margin-top:13px}

/* footer */
.site-footer{left:0;top:1163px;width:748px;height:37px;background:var(--footer);color:#cfcfcf;font-size:7.4px;text-align:center;padding-top:6px;line-height:13px}
.site-footer .phone{color:var(--red-nav)}
</style>
</head>
<body>

<header class="site-header abs">
  <div class="brand abs"><span class="brand-dot"></span>Lantern</div>
  <div class="social abs"><span></span><span></span><span></span><span></span></div>
  <nav class="nav abs">
    <a class="home" href="#">Home</a>
    <a style="left:66px" href="#">Cross The Lantern</a>
    <a style="left:156px" href="#">Performance&nbsp; Solutions</a>
    <a style="left:269px" href="#">Sustain Solutions</a>
    <a style="left:360px" href="#">Join Us</a>
    <a class="signin" style="left:412px" href="#">Sign In</a>
  </nav>
</header>

<section class="hero abs">
  <div class="intro-video abs" role="img" aria-label="Intro video area: business people shaking hands in an office">
    <svg class="play-button abs" viewBox="0 0 48 48" aria-hidden="true"><circle cx="24" cy="24" r="23" fill="rgba(255,255,255,.75)"/><path d="M19 14l15 10-15 10z" fill="#e4463a"/></svg>
    <div class="hero-caption abs">"Customer satisfaction is worthless, customer loyalty is priceless."<br><b>Harold Pennick</b></div>
  </div>
  <svg class="arrow prev abs" viewBox="0 0 24 24"><circle cx="12" cy="12" r="12" fill="#c4c4c4"/><path d="M14 7l-5 5 5 5" fill="none" stroke="#fff" stroke-width="2"/></svg>
  <svg class="arrow next abs" viewBox="0 0 24 24"><circle cx="12" cy="12" r="12" fill="#c4c4c4"/><path d="M10 7l5 5-5 5" fill="none" stroke="#fff" stroke-width="2"/></svg>
</section>

<section class="welcome abs">
  <h1>Welcome to Lantern Performance Group</h1>
  <p>Lantern Performance Group Inc. is the leading provider of profit generating and people development solutions. With the hands-on experience of best practices, the state-of-the-art technology and in-depth information we help companies increase their efficiencies and profits. Frank, honest, committed, valuable and rewarding are words that customers use to describe the quality services provided by Lantern Performance Group.</p>
  <p>Learn more about us, or find the right solutions for your specific business.We will be delighted to help you achieve better business results.</p>
</section>

<section class="who abs">
  <h2 class="section-title">Who We Are</h2>
  <div class="who-text abs">
    <p>With highly experienced performance consultants, trainers and subject matter experts based throughout the North America, Europe, the Middle East and Asia Pacific we offer unrivalled skills and expertise in designing and implementing highly interactive and proven performance solutions, aimed at developing your people and rapidly delivering increased sales and profits.</p>
    <p>We do not believe that a cookie cutter approach works in today's environment and that's why we utilize our expertise, people knowledge and various tools to provide a number of customized business solutions.</p>
    <p>We will assist you in driving towards improved sales, customer loyalty, performance indicators, processes, staff skill sets and help your business to achieve its long and short term objectives.</p>
    <p>We draw on unparalleled experience, our unique global resources and market-leading assets to help clients identify opportunities and build capabilities that underpin high performance. Certainly we will point out the low hanging fruit but consistency is what we aim for.</p>
  </div>
  <div class="who-photo abs" role="img" aria-label="Two smiling businessmen in suits"></div>
</section>

<h2 class="section-title perf-title abs">Performance <em>Solutions</em></h2>
<div class="perf-text abs">
  <p>We will work together with you to identify your needs, challenges and opportunities. We will then recommend the next steps and work with you to develop your bespoke performance solution and action plan, which will help you address those challenges. Best of all, our solutions are self funding because we create value for our customers with everything we do.</p>
  <p>Contact us now to arrange a meeting to discuss your needs and requirements.</p>
</div>
<ul class="solution-list abs">
  <li>Business Diagnostics</li>
  <li>Executive Coaching</li>
  <li class="active">Management Development</li>
  <li>Talent Management</li>
  <li>Creating Sales Culture</li>
  <li>Creating Customer Loyalty</li>
  <li>Performance Improvement Initiatives</li>
  <li>Finance &amp; Insurance Training</li>
  <li>Product Launches</li>
</ul>

<section class="sustain abs">
  <h2 class="section-title">Sustain <em>Solutions</em></h2>
  <div class="sustain-photo abs" role="img" aria-label="A single green tree on a grassy field"></div>
  <div class="sustain-text abs">
    <p>We understand that consulting and training work very well when on site but we also understand that some learning can be accomplished as effectively by other means. As a result we offer a full suite of Lantern e-Learning courses as primary and as a supporting medium.</p>
    <p>We also provide personalized webinars whereby we will host sessions one on one specifically addressing the clients needs. Feedback has been very positive as our clients comment on the benefits of cost saving (no need to travel) and time management (participant can attend at their convenience).</p>
    <p>The cornerstone of our success, however, is the Lantern Pro which allows us our clients to sustain improvements we help them achieve in first place.</p>
    <p>Contact us for more information on how we can help you sustain the results.</p>
  </div>
</section>

<footer class="site-footer abs">
  Lantern Performance Group &nbsp;|&nbsp; 58 Alder Row, Fernvale, ON K9X 2B4, Canada &nbsp;<span class="phone">T :+1.800.555.0142</span>&nbsp; Email:info@lantern-outcomes.com &nbsp;|&nbsp; Site Map<br>
  © Copyright 2011. All rights reserved.
</footer>

</body>
</html>
```